Holiday Rental Company Flyer Design (DL not A5)

Note from PixelFolk Administration: The category sizing selected is A5, however the project requires DL sized artwork. Please refer to the DL template link below while the 'Special Requirements' are updated accordingly.

Project Brief:
We need a double sided DL flyer designed for an up market Holiday Rental Company that portrays a personalised approach to property management. These are to be used for letter box drops to homes we're specifically targeting so the design should be modern, complimentary colour palette, uncluttered & visually appealing.

Please Download the DL Template from Quillmark here: http://www.quillmark.com.au/qm/ns/propath/UploadResources.aspx?selectedTab=0?pfid=BFB&pf_id=BFB&xnav=easypath-upload-image#Templates

Target Market(s)

Wealthy Home Owners

Industry/Entity Type

It Company

Font styles to use
Other font styles liked:
• Avant Garde Extra Light & Demi

Colors
33b8a4

Requirements
Must have
• DL Flyer sizes (210mm width x 99mm width, plus 3mm bleed)
• Front: Logo, Main Image & Grab
• Back: Contact Details & Brief Description of our business
• Images: Ideally the main image should be the house with the pool but alternatively a lifestyle images could also be used.
Nice to have
• A creative designer!
Should not have
• Clutter & busy designs

```html
<!DOCTYPE html>
<html lang="en">
<head>
<meta charset="utf-8">
<title>Harbourline Stays – DL Flyer</title>
<link rel="stylesheet" href="https://fonts.googleapis.com/css2?family=Questrial&family=Didact+Gothic&family=Barlow:wght@300;400;600&display=swap">
<style>
  :root{
    --bg:#ececec;
    --paper:#ffffff;
    --blue:#7ea3d8;
    --blue-text:#6b8fd0;
    --purple:#a083a8;
    --purple-text:#9a6fa4;
    --navy:#4b4a78;
    --text:#7a7a7a;
    --dark:#555555;
    --rule:#6d6d6d;
  }
  *{box-sizing:border-box;margin:0;padding:0}
  html,body{width:1200px;height:949px;overflow:hidden;background:var(--bg)}
  .canvas{position:relative;width:1200px;height:949px}
  .panel{position:absolute;top:126px;width:333px;height:698px;background:var(--paper);overflow:hidden}
  .panel--back{left:238px}
  .panel--front{left:624px}

  /* back */
  .headline{position:absolute;left:21px;top:40px;font-family:"Questrial",sans-serif;font-size:22px;letter-spacing:-.2px;color:var(--blue-text);white-space:nowrap}
  .headline em{font-style:normal;color:var(--purple-text)}
  .headline-rule{position:absolute;left:19px;top:74px;width:314px;height:2px;background:var(--rule)}
  .headline-rule::after{content:"";position:absolute;left:0;top:1px;border-left:13px solid transparent;border-right:13px solid transparent;border-top:12px solid var(--rule)}
  .intro{position:absolute;left:19px;top:114px;width:295px;font-family:"Didact Gothic",sans-serif;font-size:12.2px;line-height:18px;color:var(--text)}
  .service{position:absolute;left:0;top:201px;width:333px;height:270px;background:var(--blue);color:#fff;font-family:"Didact Gothic",sans-serif}
  .service-lead{position:absolute;left:19px;top:24px;width:300px;font-size:12px;line-height:19px;text-transform:uppercase}
  .service-list{list-style:none;position:absolute;left:19px;top:105px;width:300px}
  .service-list li{position:relative;padding-left:22px;font-size:12px;line-height:17px;letter-spacing:-.2px;margin-bottom:18px}
  .service-list li::before{content:"";position:absolute;left:0;top:2px;border-top:8px solid transparent;border-bottom:8px solid transparent;border-left:10px solid #fff}
  .service-list li:nth-child(2){margin-bottom:26px}
  .enquiry{position:absolute;left:19px;top:488px;width:295px;font-family:"Didact Gothic",sans-serif;font-size:12.8px;line-height:17px;color:var(--text)}
  .contact{position:absolute;left:0;top:567px;width:333px;height:131px;background:var(--purple);color:#fff;font-family:"Didact Gothic",sans-serif}
  .contact-list{list-style:none;position:absolute;left:17px;top:27px}
  .contact-list li{display:flex;align-items:center;gap:6px;font-size:10.5px;height:20px}
  .contact-list svg{width:14px;height:14px;flex:none}
  .brand-small{position:absolute;right:16px;top:46px;display:flex;align-items:center;gap:7px;font-family:"Questrial",sans-serif;font-size:12px;letter-spacing:1.5px;text-transform:uppercase;color:#fff;text-align:left;line-height:15px}
  .brand-small .dot{width:14px;height:14px;border:1.5px solid #fff;border-radius:50%}

  /* front */
  .bar{position:absolute}
  .bar--purple-top{left:0;top:69px;width:31px;height:258px;background:var(--purple)}
  .bar--navy-top{left:304px;top:69px;width:29px;height:258px;background:var(--navy)}
  .bar--navy-bottom{left:0;top:335px;width:31px;height:133px;background:var(--navy)}
  .bar--purple-bottom{left:304px;top:335px;width:29px;height:133px;background:var(--purple)}
  .hero-photo{position:absolute;left:36px;top:69px;width:261px;height:258px;
    background:linear-gradient(180deg,#15183a 0%,#2b2c52 30%,#6b5a3a 55%,#a88a55 68%,#2f6fb8 82%,#6fb4ee 100%)}
  .brand-block{position:absolute;left:36px;top:335px;width:261px;height:133px;background:var(--blue);display:flex;flex-direction:column;align-items:center;justify-content:center;gap:12px}
  .brand-name{font-family:"Questrial",sans-serif;font-size:27px;line-height:30px;letter-spacing:4.5px;color:#fff;text-align:center;text-transform:uppercase}
  .brand-block .dot{width:22px;height:22px;border:1.5px solid #fff;border-radius:50%}
  .tagline{position:absolute;left:36px;top:520px;font-family:"Barlow",sans-serif;font-weight:300;font-size:23.5px;line-height:31px;color:var(--dark);text-transform:uppercase}
  .site{position:absolute;left:36px;top:651px;font-family:"Barlow",sans-serif;font-weight:600;font-size:12.5px;color:#333}
</style>
</head>
<body>
<main class="canvas">

  <section class="panel panel--back" aria-label="Flyer back">
    <h2 class="headline">WHAT WE DO <em>DIFFERENTLY!</em></h2>
    <div class="headline-rule"></div>
    <p class="intro">Rather than relying upon a key safe or a central pickup destination, a ‘Harbourline Stays’ staff member will greet guests upon arrival.</p>

    <div class="service">
      <p class="service-lead">Our ‘Meet &amp; Greet’ service provides home owners with an increased level of security and also allows us to:</p>
      <ul class="service-list">
        <li>Prepare the home for their arrival (lights, heaters, music etc.);</li>
        <li>Establish a rapport &amp; help facilitate future bookings;</li>
        <li>Reiterate their responsibilities to ensure the return of their bond.</li>
      </ul>
    </div>

    <p class="enquiry">If you’d like to know what your property could achieve or require additional information, please contact us on:</p>

    <div class="contact">
      <ul class="contact-list">
        <li><svg viewBox="0 0 14 14" fill="none" stroke="#fff" stroke-width="1.1"><circle cx="7" cy="7" r="6.2"/><path d="M4.6 3.8l1.2 1.6-.7.8c.5 1 1.3 1.8 2.3 2.3l.8-.7 1.6 1.2-.8 1.1C6.6 10 4 7.4 3.7 4.6z"/></svg>(03) 5100 2468</li>
        <li><svg viewBox="0 0 14 14" fill="none" stroke="#fff" stroke-width="1.1"><rect x="1" y="3" width="12" height="8.5"/><path d="M1 3l6 5 6-5"/></svg>stay@harbourlinestays.com.au</li>
        <li><svg viewBox="0 0 14 14" fill="none" stroke="#fff" stroke-width="1.1"><circle cx="7" cy="7" r="6"/><ellipse cx="7" cy="7" rx="2.6" ry="6"/><path d="M1 7h12M2 4h10M2 10h10"/></svg>harbourlinestays.com.au</li>
        <li><svg viewBox="0 0 14 14" fill="none" stroke="#fff" stroke-width="1.1"><path d="M1 7.5L7 2l6 5.5M3 6.2V12.5h8V6.2"/><path d="M6 12.5V9h2v3.5"/></svg>PO Box 12, Elmsford Victoria 3999</li>
      </ul>
      <div class="brand-small"><span class="dot"></span><span>Harbourline<br>Stays</span></div>
    </div>
  </section>

  <section class="panel panel--front" aria-label="Flyer front">
    <div class="bar bar--purple-top"></div>
    <div class="bar bar--navy-top"></div>
    <div class="hero-photo" role="img" aria-label="Photo of a modern luxury holiday home at dusk with lit interiors and a glowing blue pool"></div>
    <div class="bar bar--navy-bottom"></div>
    <div class="brand-block">
      <p class="brand-name">Harbourline<br>Stays</p>
      <span class="dot"></span>
    </div>
    <div class="bar bar--purple-bottom"></div>
    <h1 class="tagline">Holiday rental<br>management with<br>a difference</h1>
    <p class="site">www.harbourlinestays.com.au</p>
  </section>

</main>
</body>
</html>
```